Design A Beginners Ketogenic Recipe Book Cover

I'm looking for a recipe book cover that looks professional, and incoporates "The Lantern Hollow Cookbook". I have plenty more recipe photos if needed, but would love a pro's take on the graphic design.

Its targeted at beginners of the ketogenic diet, and I would like it to highlight a similar design from my website and graphics found at https://www.bramblecovekitchen.com.au/

Target Market(s)

American / Australian / Canadian Females - Ages from 35 - 50. Interested in weight loss, diets, ketogenic diet.

Industry/Entity Type

Cooking

Font styles to use
Serif

Colors
33a6d7
0692cd
85cae6
cee9f5

Requirements
Must have
• Must include my logo, must include title "The Lantern Hollow Cookbook"
Nice to have
• I don't have a strong idea for the cook book, but If you reseach cookbooks you'll get a good idea on what a cookbook should look like.

```html
<!DOCTYPE html>
<html lang="en">
<head>
<meta charset="utf-8">
<title>The Lantern Hollow Cookbook — Cover</title>
<link rel="stylesheet" href="https://fonts.googleapis.com/css2?family=Barlow+Semi+Condensed:wght@700&family=Roboto+Slab:wght@800&family=Allura&display=swap">
<style>
  :root {
    --stage: #c6c6c6;
    --frame-blue: #0692cd;
    --brand-blue: #33a6d7;
    --sky-blue: #85cae6;
    --pale-blue: #cee9f5;
    --paper: #ffffff;
    --title-white: #ffffff;
    --cookie-light: #e6c48e;
    --cookie-gold: #d4a464;
    --cookie-bake: #b57a3c;
    --chip-brown: #5a3520;
    --tray-dark: #3a3a3c;
    --wood-grey: #9a9ea4;
    --band-veil: rgba(255, 255, 255, 0.2);
  }
  * { box-sizing: border-box; margin: 0; padding: 0; }
  html, body {
    width: 900px;
    height: 1200px;
    overflow: hidden;
    background: var(--stage);
  }
  .cover {
    position: absolute;
    left: 110px;
    top: 120px;
    width: 678px;
    height: 960px;
    background: var(--frame-blue);
    padding: 20px;
  }
  .cover__inner {
    position: relative;
    width: 100%;
    height: 100%;
    background: var(--paper);
    overflow: hidden;
  }
  .brand {
    position: absolute;
    left: 213px;
    top: 40px;
    display: flex;
    align-items: center;
    gap: 14px;
  }
  .brand__mark {
    width: 96px;
    height: 98px;
    background: var(--sky-blue);
  }
  .brand__name {
    font-family: "Barlow Semi Condensed", Arial, sans-serif;
    font-weight: 700;
    font-size: 32px;
    line-height: 36px;
    color: var(--brand-blue);
    text-transform: uppercase;
  }
  .hero-photo {
    position: absolute;
    left: 0;
    top: 150px;
    width: 100%;
    height: 770px;
    background:
      radial-gradient(ellipse 52% 14% at 48% 8%, var(--cookie-light) 0%, var(--cookie-gold) 70%, rgba(212,164,100,0) 100%),
      radial-gradient(ellipse 40% 30% at 50% 45%, rgba(90,53,32,0.25) 0%, rgba(90,53,32,0) 70%),
      radial-gradient(ellipse 58% 50% at 52% 46%, var(--cookie-light) 0%, var(--cookie-gold) 55%, var(--cookie-bake) 78%, rgba(181,122,60,0) 96%),
      linear-gradient(180deg, #ffffff 0%, #eef0f2 6%, #d8d6d3 40%, #8c7f73 70%, var(--tray-dark) 84%, var(--tray-dark) 92%, var(--wood-grey) 100%);
  }
  .title-band {
    position: absolute;
    left: 0;
    top: 322px;
    width: 100%;
    height: 318px;
    background: var(--band-veil);
  }
  .title {
    position: absolute;
    inset: 0;
    color: var(--title-white);
  }
  .title__lead {
    position: absolute;
    left: 52px;
    top: 340px;
    font-family: "Roboto Slab", Georgia, serif;
    font-weight: 800;
    font-size: 48px;
    line-height: 1;
    text-shadow: 0 1px 4px rgba(0,0,0,0.3);
  }
  .title__script {
    position: absolute;
    left: 30px;
    top: 398px;
    font-family: "Allura", cursive;
    font-size: 104px;
    line-height: 1;
    white-space: nowrap;
    text-shadow: 0 2px 6px rgba(0,0,0,0.3);
  }
  .title__box {
    position: absolute;
    left: 220px;
    top: 532px;
    width: 368px;
    height: 84px;
    background: var(--frame-blue);
    display: flex;
    align-items: center;
    justify-content: center;
    font-family: "Roboto Slab", Georgia, serif;
    font-weight: 800;
    font-size: 46px;
    letter-spacing: 1px;
    text-transform: uppercase;
  }
</style>
</head>
<body>
  <main class="cover">
    <div class="cover__inner">
      <div class="hero-photo" role="img" aria-label="Photograph of a tall stack of golden low-carb ketogenic chocolate chip cookies on a dark baking tray, beginner-friendly keto baking"></div>
      <div class="title-band"></div>

      <header class="brand">
        <div class="brand__mark"></div>
        <div class="brand__name">Bramble<br>Cove<br>Kitchen</div>
      </header>

      <h1 class="title">
        <span class="title__lead">THE</span>
        <span class="title__script">Lantern Hollow</span>
        <span class="title__box">Cookbook</span>
      </h1>
    </div>
  </main>
</body>
</html>
```